Criação de Papelaria Profissional para Advocacia e Direito
A empresa queria:
" Somos um escritório de advocacia full-service, com sede em Santarém-PA e uma unidade em Manaus-AM. Temos atuação em todo o Brasil. "

```html
<!DOCTYPE html>
<html lang="pt-BR">
<head>
<meta charset="UTF-8">
<title>Assinatura de e-mail — Henrique Valadares</title>
<link rel="stylesheet" href="https://fonts.googleapis.com/css2?family=Cormorant+Garamond:wght@500&family=Montserrat:wght@400;500;600&display=swap">
<style>
  :root {
    --page-bg: #f1f1ec;
    --navy: #1b2c45;
    --navy-deep: #15233a;
    --gold: #c8b58e;
    --ink-light: #e6e3dc;
    --ink-muted: #b9bec8;
    --rule: rgba(200, 181, 142, 0.45);
  }
  * { margin: 0; padding: 0; box-sizing: border-box; }
  html, body { width: 1200px; height: 1200px; overflow: hidden; }
  body {
    background: var(--page-bg);
    font-family: "Montserrat", sans-serif;
    display: flex; align-items: center; justify-content: center;
  }
  .signature {
    position: relative;
    width: 1100px; height: 262px;
    background: linear-gradient(100deg, var(--navy) 0%, var(--navy-deep) 100%);
    color: var(--ink-light);
    overflow: hidden;
    white-space: nowrap;
  }
  .brand {
    position: absolute; left: 42px; top: 60px;
    display: flex; align-items: center; gap: 12px;
  }
  .brand-square { width: 32px; height: 32px; border: 2px solid var(--gold); flex: none; }
  .brand-text { display: flex; flex-direction: column; gap: 5px; }
  .brand-name { font-size: 19px; font-weight: 500; letter-spacing: 0.3px; color: var(--ink-light); }
  .brand-tagline { font-size: 7px; letter-spacing: 2.6px; color: var(--ink-muted); text-align: center; }

  .person { position: absolute; left: 384px; top: 52px; }
  .person-name {
    font-family: "Cormorant Garamond", serif; font-weight: 500;
    font-size: 25px; letter-spacing: 1px; color: var(--ink-muted);
  }
  .person-role { font-size: 14px; color: var(--ink-light); margin-top: 8px; }
  .person-reg { font-size: 13px; color: var(--ink-light); margin-top: 6px; }

  .contacts-main { position: absolute; left: 748px; top: 56px; }
  .contact-line { display: flex; align-items: center; gap: 9px; font-size: 14px; margin-bottom: 11px; }
  .contact-line svg { width: 14px; height: 14px; flex: none; }
  .website { font-size: 17px; font-weight: 600; margin-top: 4px; color: var(--ink-light); }

  .rule { position: absolute; left: 42px; right: 42px; top: 156px; height: 1px; background: var(--rule); }

  .unit { position: absolute; top: 176px; }
  .unit-title { font-size: 14px; font-weight: 600; margin: 0 0 8px 20px; }
  .unit .contact-line { font-size: 12.5px; margin-bottom: 8px; }
  .unit .contact-line svg { width: 12px; height: 12px; }
  .unit-main { left: 52px; }
  .unit-manaus { left: 560px; }

  .address { position: absolute; top: 206px; display: flex; gap: 9px; font-size: 12.5px; line-height: 1.6; }
  .address svg { width: 12px; height: 14px; margin-top: 9px; flex: none; }
  .address-main { left: 300px; }
  .address-manaus { left: 836px; }
</style>
</head>
<body>
  <svg width="0" height="0" style="position:absolute">
    <defs>
      <symbol id="icon-phone" viewBox="0 0 24 24"><path fill="#c8b58e" d="M6.6 10.8a15.5 15.5 0 0 0 6.6 6.6l2.2-2.2a1 1 0 0 1 1-.25 11.4 11.4 0 0 0 3.6.57 1 1 0 0 1 1 1V20a1 1 0 0 1-1 1A17 17 0 0 1 3 4a1 1 0 0 1 1-1h3.5a1 1 0 0 1 1 1c0 1.25.2 2.46.57 3.6a1 1 0 0 1-.25 1z"/></symbol>
      <symbol id="icon-mail" viewBox="0 0 24 24"><rect x="2.5" y="5" width="19" height="14" rx="1.5" fill="none" stroke="#c8b58e" stroke-width="2"/><path d="M3 6l9 7 9-7" fill="none" stroke="#c8b58e" stroke-width="2"/></symbol>
      <symbol id="icon-pin" viewBox="0 0 20 24"><path fill="#c8b58e" d="M10 0a8 8 0 0 0-8 8c0 6 8 16 8 16s8-10 8-16a8 8 0 0 0-8-8zm0 11a3 3 0 1 1 0-6 3 3 0 0 1 0 6z"/></symbol>
    </defs>
  </svg>

  <section class="signature" aria-label="Assinatura de e-mail">
    <div class="brand">
      <div class="brand-square"></div>
      <div class="brand-text">
        <span class="brand-name">HENRIQUE VALADARES</span>
        <span class="brand-tagline">ADVOGADOS ASSOCIADOS</span>
      </div>
    </div>

    <div class="person">
      <p class="person-name">HENRIQUE VALADARES</p>
      <p class="person-role">Fundador e Sócio Sênior</p>
      <p class="person-reg">OAB/PA 12.345</p>
    </div>

    <div class="contacts-main">
      <p class="contact-line"><svg><use href="#icon-phone"/></svg>(93) 90000-1234</p>
      <p class="contact-line"><svg><use href="#icon-mail"/></svg>contato@valadaresadv.com.br</p>
      <p class="website">valadaresadv.com.br</p>
    </div>

    <div class="rule"></div>

    <div class="unit unit-main">
      <p class="unit-title">Unidade Matriz</p>
      <p class="contact-line"><svg><use href="#icon-phone"/></svg>(93) 90000-1234</p>
      <p class="contact-line"><svg><use href="#icon-mail"/></svg>contato@valadaresadv.com.br</p>
    </div>
    <div class="address address-main">
      <svg viewBox="0 0 20 24"><use href="#icon-pin"/></svg>
      <p>Av. das Palmeiras, nº 410<br>Centro - Santarém - PA.</p>
    </div>

    <div class="unit unit-manaus">
      <p class="unit-title">Unidade Manaus</p>
      <p class="contact-line"><svg><use href="#icon-phone"/></svg>(93) 90000-5678</p>
      <p class="contact-line"><svg><use href="#icon-mail"/></svg>manaus@valadaresadv.com.br</p>
    </div>
    <div class="address address-manaus">
      <svg viewBox="0 0 20 24"><use href="#icon-pin"/></svg>
      <p>Rua dos Ipês, nº 88<br>Aleixo - Manaus - AM.</p>
    </div>
  </section>
</body>
</html>
```